Hearthside BBQ Co. Rub and Sauce Labels

I am bringing to market 3 different meat rubs and 2 BBQ sauces. These rubs and sauces will be sold on an eCommerce website and also at local events. I am looking for simplicity. I believe the BBQ seasoning labels out there are very busy. I am looking for each label to be similar, yet distinct enough to clearly differentiate the different rubs in my offerings. My logo is attached. The Flaming F in my logo is going to be a feature in my brand and would like to have it be a feature on my labels, too. The rubs will be packaged in a traditional clear plastic shaker with a pop-top. I am open to ideas on packaging options as well. The different rubs in the shakers will range in color from very light to dark brown, depending on the ingredients in each rub. Please include all FDA required information on the labels. The rub labels will go on a clear plastic shaker and the sauce will be packaged in a bottle. Thanks for your help and I look forward to seeing your creativity come to life!

Colors

Designer to choose colors to be used in the design.

Requirements
Must have
• Simplicity, yet ability to separate multiple products by simple changes in logo and/or packaging. Please see the attached photo of a competitors bbq sauce - something simple yet flexible.
Nice to have
• Flexibility in design.

```html
<!DOCTYPE html>
<html lang="en">
<head>
<meta charset="utf-8">
<title>Hearthside BBQ Co. Sauce Labels</title>
<link href="https://fonts.googleapis.com/css2?family=Alfa+Slab+One&family=Archivo+Black&family=Montserrat:wght@300;400;700&family=Roboto:wght@400&family=Roboto+Condensed:wght@400&display=swap" rel="stylesheet">
<style>
  :root {
    --page: #ffffff;
    --paper: #f4f4f4;
    --ink-dark: #1c1c1c;
    --accent-flame: #f28a2e;
    --gold-a: #a8660a;
    --gold-b: #7a4606;
    --gold-name: #f0c77a;
    --smoky-a: #7a1a17;
    --smoky-b: #4e0f10;
    --smoky-name: #e8958d;
    --carolina-a: #1a2a8a;
    --carolina-b: #101c5c;
    --carolina-name: #7f9ef5;
    --type-light: #ffffff;
    --type-body: #f1ede8;
  }
  * { box-sizing: border-box; margin: 0; padding: 0; }
  html, body { width: 1200px; height: 1200px; overflow: hidden; background: var(--page); }
  .canvas {
    width: 1200px; height: 1200px;
    display: flex; align-items: center; justify-content: center; gap: 30px;
  }
  .label {
    width: 366px; height: 360px;
    display: flex; position: relative;
    box-shadow: 0 6px 18px rgba(0,0,0,0.18);
  }
  .label__brand-panel {
    width: 140px; height: 100%;
    background: linear-gradient(90deg, #e6e6e6, var(--paper) 40%, #ffffff);
    display: flex; flex-direction: column; align-items: center;
    padding-top: 18px;
  }
  .brand-mark__dot {
    width: 16px; height: 16px; border-radius: 50%;
    background: var(--accent-flame); margin-bottom: 7px;
  }
  .brand-mark__name {
    font-family: "Montserrat", sans-serif; font-weight: 700;
    font-size: 10px; letter-spacing: 0.5px; line-height: 1.25;
    color: var(--ink-dark); text-align: center;
  }
  .label__flavor-panel {
    flex: 1; height: 100%;
    padding: 26px 0 0 20px;
    color: var(--type-light);
    display: flex; flex-direction: column;
  }
  .label--gold .label__flavor-panel { background: linear-gradient(90deg, var(--gold-a), var(--gold-b)); }
  .label--smoky .label__flavor-panel { background: linear-gradient(90deg, var(--smoky-a), var(--smoky-b)); }
  .label--carolina .label__flavor-panel { background: linear-gradient(90deg, var(--carolina-a), var(--carolina-b)); }
  .flavor-name {
    font-family: "Montserrat", sans-serif; font-weight: 400;
    font-size: 32px; letter-spacing: 1px; line-height: 1;
    text-align: center; padding-right: 14px;
  }
  .label--gold .flavor-name { color: var(--gold-name); }
  .label--smoky .flavor-name { color: var(--smoky-name); }
  .label--carolina .flavor-name { color: var(--carolina-name); }
  .product-word {
    font-family: "Alfa Slab One", serif; font-size: 56px;
    line-height: 1; margin-top: 8px; letter-spacing: 2px;
    transform: scaleX(1.15); transform-origin: left;
  }
  .product-type {
    font-family: "Archivo Black", sans-serif; font-size: 31px;
    line-height: 1; margin-top: 6px; padding-left: 16px; letter-spacing: 1px;
  }
  .divider {
    height: 2px; background: var(--type-body);
    margin: 16px 0 0 16px; opacity: 0.9;
  }
  .description {
    font-family: "Roboto", sans-serif; font-size: 11.5px; line-height: 1.42;
    color: var(--type-body); margin: 16px 14px 0 16px;
  }
  .net-weight {
    font-family: "Roboto Condensed", sans-serif; font-size: 12.5px;
    color: var(--type-light); margin-top: auto; margin-bottom: 20px;
    text-align: right; padding-right: 16px;
  }
</style>
</head>
<body>
<main class="canvas">
  <article class="label label--gold">
    <div class="label__brand-panel">
      <span class="brand-mark__dot"></span>
      <p class="brand-mark__name">HEARTHSIDE<br>BBQ CO.</p>
    </div>
    <div class="label__flavor-panel">
      <h2 class="flavor-name">GOLD</h2>
      <p class="product-word">BBQ</p>
      <p class="product-type">SAUCE</p>
      <div class="divider"></div>
      <p class="description">Lorem Ipsum. Proin gravida nibh vel velit auctor aliquet. Aenean sollicitudin, lorem quis bibendum auctor, nisi elit consequat ipsum, nec sagittis sem nibh id elit.</p>
      <p class="net-weight">Net Wt. 20 oz (1.25 lbs.)</p>
    </div>
  </article>
  <article class="label label--smoky">
    <div class="label__brand-panel">
      <span class="brand-mark__dot"></span>
      <p class="brand-mark__name">HEARTHSIDE<br>BBQ CO.</p>
    </div>
    <div class="label__flavor-panel">
      <h2 class="flavor-name">SMOKY</h2>
      <p class="product-word">BBQ</p>
      <p class="product-type">SAUCE</p>
      <div class="divider"></div>
      <p class="description">Lorem Ipsum. Proin gravida nibh vel velit auctor aliquet. Aenean sollicitudin, lorem quis bibendum auctor, nisi elit consequat ipsum, nec sagittis sem nibh id elit.</p>
      <p class="net-weight">Net Wt. 20 oz (1.25 lbs.)</p>
    </div>
  </article>
  <article class="label label--carolina">
    <div class="label__brand-panel">
      <span class="brand-mark__dot"></span>
      <p class="brand-mark__name">HEARTHSIDE<br>BBQ CO.</p>
    </div>
    <div class="label__flavor-panel">
      <h2 class="flavor-name">CAROLINA</h2>
      <p class="product-word">BBQ</p>
      <p class="product-type">SAUCE</p>
      <div class="divider"></div>
      <p class="description">Lorem Ipsum. Proin gravida nibh vel velit auctor aliquet. Aenean sollicitudin, lorem quis bibendum auctor, nisi elit consequat ipsum, nec sagittis sem nibh id elit.</p>
      <p class="net-weight">Net Wt. 20 oz (1.25 lbs.)</p>
    </div>
  </article>
</main>
</body>
</html>
```